Review/Re-Design Supermarket E-Commerce website

We have launched our Supermarket E-commerce Website but feel it is lacking a modern feel.

Please re-design the current Supermarket E-commerce site, creating a more modern look and feel.

I am looking for design changes to things such as:

- Fonts
- Button shape & Size
- Shapes of boxes
- Layout of drop down menus
- A new shopping cart / button
- The Header (and in particular the use and positioning of the logo)
- Supplying a generic background image (currently berries)

Please do not change the structure of the page. For instance, the category selection will always be on the left, the items will always be displayed in rows of 3 and the shopping cart should be on the right.
Updates

Current site can be found at www.brovanmarket.com.au

Project Deadline Extended
Reason: designs coming in are generally too different from current design. we are looking for less that 10% change to the overall look and feel. one aspect that needs a lot of work is the checkout cart on the right hand side. please checkout http://www2.pelkinfreshmart.com.au/?gclid=QXRP4kdmwnLBHTYEzJuaPGEKtB

Target Market(s)

Consumers buying their weekly grocery shopping online

Industry/Entity Type

Shopping

Number of Pages Required

1 page

Requirements
Must have
• Stick to the branding of the Logo. Which is Red, Blue and White.
• Other colours may be used in small percentages.
Should not have
• Do not change the Structure of the site.

```html
<!DOCTYPE html>
<html lang="en">
<head>
<meta charset="utf-8">
<title>Brovan Market – Online Shop</title>
<link href="https://fonts.googleapis.com/css2?family=Montserrat:wght@400;500;600;700&family=Open+Sans:wght@400;600&display=swap" rel="stylesheet">
<style>
:root{
  --blue:#0b5ebd;
  --red:#e8202a;
  --orange:#f7941d;
  --green:#1f7a3a;
  --line:#c9d9e6;
  --text:#555a60;
  --topbar:#f1f4f7;
  --footer:#3d3e41;
  --footer-base:#2f3033;
  --footer-text:#8d9095;
}
*{box-sizing:border-box;margin:0;padding:0}
html,body{width:1200px;height:1143px;overflow:hidden;background:#fff}
body{position:relative;font-family:"Open Sans",sans-serif;color:var(--text)}
.abs{position:absolute}
.caps{font-family:"Montserrat",sans-serif;text-transform:uppercase;letter-spacing:1.2px}

.topbar{left:0;top:0;width:1200px;height:25px;background:var(--topbar)}
.topbar-phone{left:738px;top:6px;font-size:9px;color:#444;display:flex;align-items:center;gap:8px;letter-spacing:.5px}
.topbar-social{left:832px;top:0;width:115px;height:25px;background:var(--blue);display:flex;justify-content:space-around;align-items:center;padding:0 14px}
.topbar-social span{width:8px;height:8px;background:#fff;border-radius:1px}

.header{left:0;top:25px;width:1200px;height:73px;background:#fff}
.brand{left:252px;top:51px;display:flex;align-items:center;gap:8px}
.brand-name{font-family:"Montserrat",sans-serif;font-weight:700;font-size:15px;color:var(--blue);letter-spacing:.4px;line-height:1}
.brand-mark{width:14px;height:14px;border-radius:50%;background:var(--red)}
.brand-sub{left:262px;top:68px;font-family:"Montserrat",sans-serif;font-size:8px;letter-spacing:3.4px;color:var(--blue)}
.nav{top:57px;font-size:9px;color:#444}
.nav-cart{left:893px;top:55px;display:flex;gap:8px;align-items:center;font-size:9px;color:#444}

.hero{left:0;top:98px;width:1200px;height:211px;background:linear-gradient(90deg,#8a5a2f 0%,#b77a3e 18%,#e7b52b 40%,#c98a3f 60%,#b2452a 80%,#c9782d 100%)}

.search-head{left:398px;top:214px;width:405px;height:45px;background:#fff;display:flex;align-items:center;justify-content:center;font-size:8px;color:var(--blue);font-weight:500}
.search-bar{left:398px;top:259px;width:405px;height:72px;background:var(--blue)}
.field{top:18px;height:36px;border:1.5px solid #fff;display:flex;align-items:center;justify-content:space-between;padding:0 14px;color:#fff;font-size:8px;font-weight:500}

.tab{left:244px;width:127px;height:26px;display:flex;align-items:center;gap:10px;padding-left:10px;color:#fff;font-size:8px;font-weight:600}
.tab-specials{top:309px;background:var(--red)}
.tab-favourites{top:336px;background:var(--orange)}
.categories{left:244px;top:378px;list-style:none}
.categories li{height:24.4px;font-size:8.5px;color:#555;display:flex;align-items:center;gap:8px}
.categories li::before{content:"›";font-size:10px;color:#666}

.card{width:119px;height:203px;border:1.5px solid var(--line);background:#fff;overflow:hidden}
.card-photo{position:absolute;left:16px;top:8px;width:84px;height:70px;border-radius:40%}
.card-name{position:absolute;left:0;width:100%;top:89px;text-align:center;font-family:"Montserrat",sans-serif;font-size:9px;letter-spacing:.8px;color:#555}
.card-rule{position:absolute;left:0;top:109px;width:100%;border-top:1.5px solid var(--line)}
.qty{position:absolute;left:28px;top:124px;width:60px;display:flex;justify-content:space-between;align-items:center;font-family:"Montserrat",sans-serif;font-size:9px;color:var(--blue)}
.price{position:absolute;left:12px;top:147px;font-family:"Montserrat",sans-serif;font-size:12px;font-weight:600;color:var(--blue);letter-spacing:1px}
.price s{font-size:9px;font-weight:400;color:#666;margin-left:4px;letter-spacing:.3px}
.card-btn{position:absolute;left:0;bottom:0;width:100%;height:25px;display:flex;align-items:center;justify-content:center;gap:8px;color:#fff;font-size:8px;font-weight:600;background:var(--blue)}
.card-btn.added{background:var(--orange)}
.save{position:absolute;left:0;top:0;width:56px;height:56px;background:var(--green);clip-path:polygon(0 0,100% 0,0 100%)}
.save-text{position:absolute;left:6px;top:5px;color:#fff;font-family:"Montserrat",sans-serif;font-size:7px;line-height:10px;letter-spacing:.6px}

.cart{left:829px;top:361px;width:118px;height:477px;border:1.5px solid var(--line)}
.cart-center{position:absolute;left:0;width:100%;text-align:center}
.cart-title{font-family:"Montserrat",sans-serif;font-size:8.5px;letter-spacing:1.3px;color:var(--blue)}
.cart-addr{font-family:"Montserrat",sans-serif;font-size:7px;line-height:9.5px;letter-spacing:.6px;color:#444}
.cart-rule{position:absolute;left:0;width:100%;border-top:1.5px solid var(--line)}
.cart-count{position:absolute;left:10px;top:198px;display:flex;align-items:center;gap:12px;font-family:"Montserrat",sans-serif;font-size:9.5px;letter-spacing:.8px;color:#555}
.cart-sub{position:absolute;left:10px;top:230px;width:98px;display:flex;justify-content:space-between;align-items:baseline;font-family:"Montserrat",sans-serif;font-size:7.5px;letter-spacing:.8px;color:#444}
.cart-sub b{font-size:10.5px;color:var(--blue);letter-spacing:1px}
.checkout{position:absolute;left:9px;top:257px;width:98px;height:30px;background:var(--orange);border:1.5px solid #e9781a;color:#fff;display:flex;align-items:center;justify-content:center;font-size:8.5px;font-weight:600}
.line-item{position:absolute;left:14px;width:94px;font-family:"Montserrat",sans-serif;font-size:7.5px;letter-spacing:.8px;color:#444;line-height:9px}
.line-price{position:absolute;left:14px;width:92px;display:flex;justify-content:space-between;align-items:center;font-family:"Montserrat",sans-serif;font-size:9.5px;font-weight:600;color:var(--blue);letter-spacing:1px}

.footer{left:0;top:905px;width:1200px;height:178px;background:var(--footer)}
.footer-divider{top:905px;width:1px;height:178px;background:#55575b}
.footer-links{top:951px;list-style:none}
.footer-links li{height:21.3px;font-size:9.5px;letter-spacing:1px;color:var(--footer-text)}
.store-badge{left:843px;width:104px;height:37px;background:#fff;border-radius:3px}
.footer-base{left:0;top:1083px;width:1200px;height:60px;background:var(--footer-base)}
.pay-card{top:1101px;width:34px;height:23px;background:#fff;border-radius:2px}
.copy{left:378px;top:1108px;font-size:8.5px;letter-spacing:.8px;color:#6c6f74}
.base-phone{left:666px;top:1107px;display:flex;gap:8px;align-items:center;font-size:9px;color:#d6d7d9;letter-spacing:.8px}
.base-social{top:1109px;width:7px;height:7px;background:#bfc1c4;border-radius:1px}
</style>
</head>
<body>

<div class="abs topbar"></div>
<div class="abs topbar-phone">
  <svg width="10" height="10" viewBox="0 0 10 10"><path d="M2 1l2 2-1 1.2c.6 1.3 1.5 2.2 2.8 2.8L7 6l2 2-1.3 1.3C4.5 9 1 5.5.7 2.3z" fill="#777"/></svg>
  1300 555 218
</div>
<div class="abs topbar-social"><span></span><span></span><span></span></div>

<div class="abs header"></div>
<div class="abs brand"><span class="brand-name">BROVAN MARKET</span><span class="brand-mark"></span></div>
<div class="abs brand-sub">SUPERMARKETS</div>
<div class="abs nav" style="left:695px">Products</div>
<div class="abs nav" style="left:770px">Register</div>
<div class="abs nav" style="left:844px">Login</div>
<div class="abs nav-cart">
  <svg width="16" height="12" viewBox="0 0 16 12"><path d="M1 1h2.5l2 7h7.5l1.5-5H4.5" fill="none" stroke="#555" stroke-width="1"/><circle cx="6.5" cy="10.5" r="1" fill="#555"/><circle cx="12" cy="10.5" r="1" fill="#555"/></svg>
  My Cart
</div>

<div class="abs hero" role="img" aria-label="Fresh fruit and vegetables on a wooden table"></div>

<div class="abs search-head caps">Lorem ipsum is simply dummy text of the printing</div>
<div class="abs search-bar">
  <div class="abs field caps" style="left:20px;width:134px">Search
    <svg width="10" height="10" viewBox="0 0 10 10"><circle cx="4" cy="4" r="3" fill="none" stroke="#fff" stroke-width="1.5"/><path d="M6.3 6.3L9 9" stroke="#fff" stroke-width="1.6"/></svg></div>
  <div class="abs field caps" style="left:172px;width:98px">Filter by
    <svg width="7" height="5" viewBox="0 0 7 5"><path d="M1 1l2.5 2.5L6 1" fill="none" stroke="#fff"/></svg></div>
  <div class="abs field caps" style="left:289px;width:98px">Sort by
    <svg width="7" height="5" viewBox="0 0 7 5"><path d="M1 1l2.5 2.5L6 1" fill="none" stroke="#fff"/></svg></div>
</div>

<div class="abs tab tab-specials caps">
  <svg width="10" height="10" viewBox="0 0 10 10"><path d="M5 .5l1.3 3 3.2.3-2.4 2.1.7 3.2L5 7.4 2.2 9.1l.7-3.2L.5 3.8l3.2-.3z" fill="#f7c21d"/></svg>
  Online specials</div>
<div class="abs tab tab-favourites caps">
  <svg width="11" height="10" viewBox="0 0 11 10"><path d="M1 5l4-4h5v5l-4 4z" fill="none" stroke="#e8202a" stroke-width="1.2"/><circle cx="7.5" cy="3.5" r="1" fill="#e8202a"/></svg>
  Favourites</div>
<ul class="abs categories">
  <li>Baking Needs</li><li>Baking Accessories</li><li>Beverages</li><li>Coconut</li>
  <li>Biscuits</li><li>Breakfast Foods</li><li>Cereal</li><li>Canned Food</li>
  <li>Baked Beans &amp; Spaghetti</li><li>Cheese</li><li>Blocks</li><li>Chilled Foods</li>
</ul>

<!-- product cards -->
<div class="abs card" style="left:398px;top:361px">
  <div class="card-photo" role="img" aria-label="Bunch of bananas" style="background:radial-gradient(#f7dc3a,#e9c21a 60%,#fff 72%)"></div>
  <div class="card-name">Bananas Each</div><div class="card-rule"></div>
  <div class="qty"><svg width="13" height="13"><circle cx="6.5" cy="6.5" r="6.5" fill="#e8202a"/><rect x="3.5" y="5.8" width="6" height="1.5" fill="#fff"/></svg>6<svg width="13" height="13"><circle cx="6.5" cy="6.5" r="6.5" fill="#1f7a3a"/><rect x="3.5" y="5.8" width="6" height="1.5" fill="#fff"/><rect x="5.8" y="3.5" width="1.5" height="6" fill="#fff"/></svg></div>
  <div class="price">$2.99<s>$4.67 ea</s></div>
  <div class="card-btn caps">Add to cart</div>
</div>
<div class="abs card" style="left:541px;top:361px">
  <div class="card-photo" role="img" aria-label="Red apple" style="background:radial-gradient(#c81e24,#8e1117 55%,#fff 68%)"></div>
  <div class="save"></div><div class="save-text">SAVE<br>$3.23</div>
  <div class="card-name">Fuji Apples Each</div><div class="card-rule"></div>
  <div class="qty"><svg width="13" height="13"><circle cx="6.5" cy="6.5" r="6.5" fill="#e8202a"/><rect x="3.5" y="5.8" width="6" height="1.5" fill="#fff"/></svg>6<svg width="13" height="13"><circle cx="6.5" cy="6.5" r="6.5" fill="#1f7a3a"/><rect x="3.5" y="5.8" width="6" height="1.5" fill="#fff"/><rect x="5.8" y="3.5" width="1.5" height="6" fill="#fff"/></svg></div>
  <div class="price">$2.99<s>$4.67 ea</s></div>
  <div class="card-btn added caps">Added <svg width="9" height="7"><path d="M1 3.5l2.5 2.5L8 1" fill="none" stroke="#fff" stroke-width="1.2"/></svg></div>
</div>
<div class="abs card" style="left:684px;top:361px">
  <div class="card-photo" role="img" aria-label="Halved avocado" style="background:radial-gradient(#d9d98a,#4f6b2a 55%,#fff 70%)"></div>
  <div class="card-name">Avocado Each</div><div class="card-rule"></div>
  <div class="qty"><svg width="13" height="13"><circle cx="6.5" cy="6.5" r="6.5" fill="#e8202a"/><rect x="3.5" y="5.8" width="6" height="1.5" fill="#fff"/></svg>6<svg width="13" height="13"><circle cx="6.5" cy="6.5" r="6.5" fill="#1f7a3a"/><rect x="3.5" y="5.8" width="6" height="1.5" fill="#fff"/><rect x="5.8" y="3.5" width="1.5" height="6" fill="#fff"/></svg></div>
  <div class="price">$2.99<s>$4.67 ea</s></div>
  <div class="card-btn caps">Add to cart</div>
</div>
<div class="abs card" style="left:398px;top:591px">
  <div class="card-photo" role="img" aria-label="Pile of blueberries" style="background:radial-gradient(#4b5a80,#2b3550 55%,#fff 70%)"></div>
  <div class="card-name">Blueberries punnet</div><div class="card-rule"></div>
  <div class="qty"><svg width="13" height="13"><circle cx="6.5" cy="6.5" r="6.5" fill="#e8202a"/><rect x="3.5" y="5.8" width="6" height="1.5" fill="#fff"/></svg>6<svg width="13" height="13"><circle cx="6.5" cy="6.5" r="6.5" fill="#1f7a3a"/><rect x="3.5" y="5.8" width="6" height="1.5" fill="#fff"/><rect x="5.8" y="3.5" width="1.5" height="6" fill="#fff"/></svg></div>
  <div class="price">$2.99<s>$4.67 ea</s></div>
  <div class="card-btn added caps">Added <svg width="9" height="7"><path d="M1 3.5l2.5 2.5L8 1" fill="none" stroke="#fff" stroke-width="1.2"/></svg></div>
</div>
<div class="abs card" style="left:541px;top:591px">
  <div class="card-photo" role="img" aria-label="Dried dates" style="background:radial-gradient(#8a3a2a,#4a1a14 55%,#fff 70%)"></div>
  <div class="card-name">Fuji Apples Each</div><div class="card-rule"></div>
  <div class="qty"><svg width="13" height="13"><circle cx="6.5" cy="6.5" r="6.5" fill="#e8202a"/><rect x="3.5" y="5.8" width="6" height="1.5" fill="#fff"/></svg>6<svg width="13" height="13"><circle cx="6.5" cy="6.5" r="6.5" fill="#1f7a3a"/><rect x="3.5" y="5.8" width="6" height="1.5" fill="#fff"/><rect x="5.8" y="3.5" width="1.5" height="6" fill="#fff"/></svg></div>
  <div class="price">$2.99<s>$4.67 ea</s></div>
  <div class="card-btn caps">Add to cart</div>
</div>
<div class="abs card" style="left:684px;top:591px">
  <div class="card-photo" role="img" aria-label="Oranges with a cut half" style="background:radial-gradient(#fbb03b,#f0891a 55%,#fff 70%)"></div>
  <div class="card-name">Avocado Each</div><div class="card-rule"></div>
  <div class="qty"><svg width="13" height="13"><circle cx="6.5" cy="6.5" r="6.5" fill="#e8202a"/><rect x="3.5" y="5.8" width="6" height="1.5" fill="#fff"/></svg>6<svg width="13" height="13"><circle cx="6.5" cy="6.5" r="6.5" fill="#1f7a3a"/><rect x="3.5" y="5.8" width="6" height="1.5" fill="#fff"/><rect x="5.8" y="3.5" width="1.5" height="6" fill="#fff"/></svg></div>
  <div class="price">$2.99<s>$4.67 ea</s></div>
  <div class="card-btn caps">Add to cart</div>
</div>

<!-- cart -->
<aside class="abs cart">
  <div class="cart-center" style="top:17px"><svg width="26" height="26"><circle cx="13" cy="13" r="13" fill="#1f7a3a"/><path d="M9 10h8l-1 8h-6z" fill="#fff"/><path d="M11 10V8.5a2 2 0 014 0V10" fill="none" stroke="#fff"/></svg></div>
  <div class="cart-center cart-title" style="top:50px">CLICK&amp;COLLECT</div>
  <div class="cart-center cart-addr" style="top:66px">Click&amp;Collect<br>4/12-18 Marlow Street<br>Brovan TAS 7290</div>
  <div class="cart-center" style="top:113px"><svg width="26" height="26"><circle cx="13" cy="13" r="13" fill="#0b5ebd"/><rect x="6" y="9" width="9" height="7" fill="#fff"/><path d="M15 11h3l2 2.5V16h-5z" fill="#fff"/><circle cx="9" cy="17" r="1.5" fill="#fff"/><circle cx="17" cy="17" r="1.5" fill="#fff"/></svg></div>
  <div class="cart-center cart-title" style="top:146px">DELIVERY INFO</div>
  <div class="cart-rule" style="top:181px"></div>
  <div class="cart-count"><svg width="22" height="18" viewBox="0 0 22 18"><path d="M1 2h4l3 10h10l2-7H6" fill="none" stroke="#0b5ebd" stroke-width="1.4"/><path d="M7 7h12M8 9.5h10" stroke="#0b5ebd"/><circle cx="9" cy="15.5" r="1.4" fill="#0b5ebd"/><circle cx="16" cy="15.5" r="1.4" fill="#0b5ebd"/></svg>3 items</div>
  <div class="cart-sub">SUB TOTAL <b>$24.00</b></div>
  <div class="checkout caps">Checkout</div>
  <div class="cart-rule" style="top:306px"></div>
  <div class="line-item" style="top:318px">1x ROSE GLOW Apples Each</div>
  <div class="line-price" style="top:342px">$0.60<svg width="12" height="12"><circle cx="6" cy="6" r="5.3" fill="none" stroke="#9bb3c9"/><path d="M4 4l4 4M8 4l-4 4" stroke="#9bb3c9"/></svg></div>
  <div class="cart-rule" style="top:363px"></div>
  <div class="line-item" style="top:376px">1x Fuji Apples Each</div>
  <div class="line-price" style="top:396px">$0.60<svg width="12" height="12"><circle cx="6" cy="6" r="5.3" fill="none" stroke="#9bb3c9"/><path d="M4 4l4 4M8 4l-4 4" stroke="#9bb3c9"/></svg></div>
  <div class="cart-rule" style="top:417px"></div>
  <div class="line-item" style="top:430px">1x Fuji Apples Each</div>
  <div class="line-price" style="top:450px">$0.60<svg width="12" height="12"><circle cx="6" cy="6" r="5.3" fill="none" stroke="#9bb3c9"/><path d="M4 4l4 4M8 4l-4 4" stroke="#9bb3c9"/></svg></div>
</aside>

<!-- footer -->
<footer>
  <div class="abs footer"></div>
  <div class="abs footer-divider" style="left:403px"></div>
  <div class="abs footer-divider" style="left:612px"></div>
  <ul class="abs footer-links" style="left:254px"><li>My Account</li><li>My Past Orders</li><li>Online Specials</li><li>Everyday Specials</li></ul>
  <ul class="abs footer-links" style="left:461px"><li>Delivery</li><li>FAQ</li><li>Privacy Policy</li><li>Terms &amp; Conditions</li></ul>
  <ul class="abs footer-links" style="left:666px"><li>About Tallo</li><li>About Us</li><li>End User License</li><li>Agreement</li></ul>
  <div class="abs store-badge" style="top:947px"></div>
  <div class="abs store-badge" style="top:992px"></div>
  <div class="abs footer-base"></div>
  <div class="abs pay-card" style="left:252px"></div>
  <div class="abs pay-card" style="left:289px"></div>
  <div class="abs pay-card" style="left:329px"></div>
  <div class="abs copy">© Tallo Pty Ltd 2014 · All Rights Reserved ver 1.1.5</div>
  <div class="abs base-phone"><svg width="10" height="10" viewBox="0 0 10 10"><path d="M2 1l2 2-1 1.2c.6 1.3 1.5 2.2 2.8 2.8L7 6l2 2-1.3 1.3C4.5 9 1 5.5.7 2.3z" fill="#bfc1c4"/></svg>1300 555 218</div>
  <div class="abs base-social" style="left:858px"></div>
  <div class="abs base-social" style="left:886px"></div>
  <div class="abs base-social" style="left:916px"></div>
</footer>

</body>
</html>
```